Flyer Design Project

I need a cool design that describes a new line of services I am selling. The final product should be a 8 1/2 by 11 and maximum two pages.

I am selling consulting services to learn to use web conferencing tools for business development, meeting and training.
Updates

Please use the file I have attached as a guide for your work. It is a document called "ebook-costsavingtips" and I love its design.

Thanks

                                        Please substitute the new text availble and just uploaded in the FLYER. Please submit the FINAL version fo your design with TExt changes as well as improvements detailed in previous message. 

Target Market(s)

Entrepreneurs and classroom educators who wnats to explore a new way to teach (innovators not scared of technology)

Industry/Entity Type

Business

Requirements
Must have
• I would like to receive a final PDF with the content EDITABLE for minor edits (I have acrobat)
Logo should be included (attached)

PLEASE CHECK OUT ATTACHED DOCUMENT WHOSE DESIGN I LOVE.
IT is called "Ebook cost-savings tips". If you could follow that as a template to design mine that would be great!

```html
<!DOCTYPE html>
<html lang="en">
<head>
<meta charset="utf-8">
<title>Online Meeting Skills Services – Flyer</title>
<link rel="stylesheet" href="https://fonts.googleapis.com/css2?family=Arimo:ital,wght@0,400;0,700;1,400&display=swap">
<style>
  :root {
    --stage: #eceef0;
    --paper: #ffffff;
    --blue: #1f6fb8;
    --blue-deep: #14508c;
    --blue-soft: #cfe2f3;
    --blue-mist: #e8f1fa;
    --photo-light: #c9d6e2;
    --photo-dark: #6f8497;
    --ink: #2b2f33;
  }
  * { box-sizing: border-box; margin: 0; padding: 0; }
  html, body { width: 1200px; height: 900px; overflow: hidden; }
  body {
    background: var(--stage);
    font-family: "Arimo", Arial, sans-serif;
    color: var(--ink);
    position: relative;
  }
  .page {
    position: absolute;
    top: 178px;
    width: 420px;
    height: 544px;
    background: var(--paper);
    box-shadow: 0 2px 10px rgba(0,0,0,.12);
    overflow: hidden;
  }
  .page--cover { left: 150px; background: linear-gradient(180deg, #fff 0%, #fff 55%, var(--blue-mist) 100%); }
  .page--back { left: 630px; }

  .swoosh { position: absolute; left: 0; bottom: 0; width: 100%; height: 110px; }

  /* brand */
  .brand { display: flex; align-items: center; gap: 6px; color: var(--blue); font-weight: 700; }
  .brand__mark { width: 10px; height: 10px; background: var(--blue); }
  .cover__brand { position: absolute; top: 48px; left: 150px; font-size: 17px; }
  .cover__brand .brand__mark { width: 13px; height: 13px; }

  /* cover */
  .cover__rule { position: absolute; left: 40px; top: 90px; width: 2px; height: 380px; background: var(--blue); }
  .cover__photo {
    position: absolute; left: 60px; top: 95px; width: 340px; height: 170px;
    background: linear-gradient(135deg, var(--photo-light) 0%, #aebfcf 45%, var(--photo-dark) 100%);
  }
  .cover__block { position: absolute; left: 22px; top: 155px; width: 38px; height: 80px; background: var(--blue); }
  .cover__title { position: absolute; left: 150px; top: 378px; width: 250px; font-weight: 700; line-height: 1.2; }
  .cover__title-main { display: block; font-size: 21px; color: var(--blue); }
  .cover__title-sub { display: block; font-size: 21px; color: var(--blue-deep); margin-top: 2px; }

  /* back page */
  .back__header {
    position: absolute; top: 20px; left: 28px; right: 28px;
    display: flex; justify-content: space-between; align-items: flex-end;
    padding-bottom: 5px; border-bottom: 1.5px solid var(--blue);
  }
  .back__header .brand { font-size: 10px; }
  .back__label { font-size: 9px; font-weight: 700; color: var(--blue); letter-spacing: .4px; }
  .back__content { position: absolute; top: 52px; left: 28px; right: 28px; }
  .back__heading { font-size: 10px; font-weight: 700; color: var(--blue); line-height: 1.25; margin: 8px 0 4px; }
  .back__content p, .back__content li { font-size: 6.4px; line-height: 1.42; margin-bottom: 4px; }
  .back__lead { font-weight: 700; }
  .back__list { list-style: none; margin: 0 0 4px; }
  .back__list li { position: relative; padding-left: 9px; }
  .back__list li::before { content: ""; position: absolute; left: 1px; top: 2.4px; width: 3.5px; height: 3.5px; background: var(--blue); }
  .service-name { font-weight: 700; color: var(--blue-deep); }
</style>
</head>
<body>

<section class="page page--cover" aria-label="Flyer cover">
  <div class="brand cover__brand"><span class="brand__mark"></span>Convenia Consulting</div>
  <div class="cover__rule"></div>
  <div class="cover__photo" role="img" aria-label="Photo of a glass piggy bank resting on a computer keyboard"></div>
  <div class="cover__block"></div>
  <h1 class="cover__title">
    <span class="cover__title-main">Online Meeting Skills Services:</span>
    <span class="cover__title-sub">It is just the beginning…</span>
  </h1>
  <svg class="swoosh" viewBox="0 0 420 110" preserveAspectRatio="none" aria-hidden="true">
    <path d="M0 70 C120 30 260 100 420 40 L420 110 L0 110 Z" fill="#dbe9f6"/>
    <path d="M0 92 C140 60 280 110 420 70 L420 110 L0 110 Z" fill="#b9d4ee"/>
  </svg>
</section>

<section class="page page--back" aria-label="Flyer reverse">
  <header class="back__header">
    <div class="brand"><span class="brand__mark"></span>Convenia Consulting</div>
    <div class="back__label">ONLINE MEETING SKILLS SERVICES</div>
  </header>

  <div class="back__content">
    <h2 class="back__heading">What if your business can reach all the people already interested in learning what you know?</h2>
    <p class="back__lead">A different use of webinar technology, the first step towards a new way of thinking about your marketplace clients.</p>
    <p>You probably know your audience and what they want to learn. Online meeting tools let you share that knowledge with people anywhere, save travel time and costs, and build lasting relationships with the clients who value your expertise. We help you plan, design and deliver sessions that keep every participant engaged.</p>
    <ul class="back__list">
      <li>We design an effective virtual meeting experience for you using the tools of the online meeting room.</li>
      <li>We repurpose your traditional marketing materials into clear and engaging online presentations.</li>
      <li>We coach you to present with confidence and to manage questions, polls and chat in real time.</li>
      <li>We support you before, during and after each session so nothing is left to chance.</li>
    </ul>

    <h2 class="back__heading">Choose the service that best fit your needs and budget. A new level of online engagement and virtual collaboration awaits.</h2>
    <ul class="back__list">
      <li><span class="service-name">Webinar Starter:</span> one coaching session to set up your first online meeting room, test your audio and rehearse your opening.</li>
      <li><span class="service-name">Presenter Package:</span> three sessions to design, practise and deliver a complete webinar for your clients or students, with feedback after each run.</li>
      <li><span class="service-name">Classroom Online:</span> a program for educators who want to move lessons into a virtual room and keep learners active.</li>
      <li><span class="service-name">Team Collaboration:</span> custom training for staff who meet, plan and share documents online across several locations.</li>
    </ul>

    <h2 class="back__heading">You'll participate via the BridgeRoom Meeting platform. No special software is required. If you have a computer with Internet access and a direct telephone line you have all is needed to participate.</h2>
    <p>As a small business owner you know that webinar technology is here to stay. Our team will guide you step by step so that your first online event feels natural, professional and worth every minute for the people who attend.</p>
  </div>

  <svg class="swoosh" viewBox="0 0 420 110" preserveAspectRatio="none" aria-hidden="true">
    <path d="M0 85 C120 60 260 110 420 72 L420 110 L0 110 Z" fill="#dbe9f6"/>
    <path d="M0 100 C140 82 280 112 420 92 L420 110 L0 110 Z" fill="#b9d4ee"/>
  </svg>
</section>

</body>
</html>
```